Pet business needs a business card

Pet shop needs a business card. Like dark background and and debased look.

Hedgerowpups
Lindelaan 27
B - 3270 Korbeek
Belgium

www.hedgerowpups.example
mail@hedgerowpups.example
Phone +32471869203

I will ad a tagline shortly.

Industry/Entity Type

Shop

Font styles to use
Sans Serif

Requirements
Must have
• Must be possible to print the card debased. See example image.

```html
<!DOCTYPE html>
<html lang="en">
<head>
<meta charset="utf-8">
<title>Hedgerowpups – Business Card</title>
<link rel="stylesheet" href="https://fonts.googleapis.com/css2?family=Open+Sans:wght@400;700&family=Metamorphous&display=swap">
<style>
  :root {
    --page: #ffffff;
    --card-dark: #1f2631;
    --brand-orange: #f7952a;
    --brand-olive: #6b6e4f;
    --ink: #1f2631;
  }
  html, body {
    margin: 0;
    padding: 0;
    width: 1108px;
    height: 1200px;
    overflow: hidden;
    background: var(--page);
  }
  .sheet {
    position: relative;
    width: 1108px;
    height: 1200px;
  }
  .card {
    position: absolute;
    left: 135px;
    width: 845px;
    height: 504px;
    display: block;
    box-shadow: 0 4px 14px rgba(0, 0, 0, 0.35);
  }
  .card--front { top: 81px; }
  .card--back { top: 627px; }
  .card-bg { fill: var(--card-dark); }
  .brand-name {
    font-family: "Open Sans", sans-serif;
    font-weight: 700;
    fill: var(--brand-orange);
  }
  .shop-title {
    font-family: "Metamorphous", serif;
    fill: var(--brand-orange);
    font-size: 54px;
    letter-spacing: 3px;
  }
  .wave-orange { fill: var(--brand-orange); }
  .wave-olive { fill: none; stroke: var(--brand-olive); stroke-width: 6; }
  .wave-dark { fill: none; stroke: var(--card-dark); stroke-width: 3; }
  .contact {
    font-family: "Open Sans", sans-serif;
    font-size: 26px;
    fill: var(--ink);
  }
  .icon { fill: none; stroke: var(--ink); stroke-width: 2.2; }
  .icon-solid { fill: var(--ink); }
</style>
</head>
<body>
<main class="sheet">

  <svg class="card card--front" viewBox="0 0 908 542" role="group" aria-label="Card front">
    <rect class="card-bg" width="908" height="542"/>
    <text class="brand-name" x="454" y="300" font-size="76" text-anchor="middle">Hedgerowpups</text>
  </svg>

  <svg class="card card--back" viewBox="0 0 908 542" role="group" aria-label="Card back">
    <rect class="card-bg" width="908" height="542"/>
    <text class="brand-name" x="100" y="160" font-size="44">Hedgerowpups</text>
    <text class="shop-title" x="485" y="150">PET SHOP</text>

    <path class="wave-orange" d="M0 245 C 150 305, 380 295, 600 238 S 850 190, 908 258 L908 542 L0 542 Z"/>
    <path class="wave-dark" d="M0 258 C 150 300, 330 300, 440 240"/>
    <path class="wave-olive" d="M30 275 C 200 305, 420 280, 620 225 S 820 185, 890 215"/>

    <g class="address-block">
      <path class="icon-solid" d="M84 385 L98 374 L112 385 Z"/>
      <rect class="icon" x="87" y="386" width="22" height="14"/>
      <line class="icon" x1="98" y1="386" x2="98" y2="400"/>
      <text class="contact" x="130" y="378">Lindelaan 27</text>
      <text class="contact" x="130" y="412">B - 3270 Korbeek</text>
      <text class="contact" x="130" y="445">Belgium</text>
    </g>

    <g class="contact-block">
      <path class="icon" d="M480 343 l6 -2 l5 9 l-4 4 c2 6 5 10 10 13 l4 -4 l8 6 l-2 6 c-14 0 -27 -16 -27 -32 Z"/>
      <text class="contact" x="520" y="366">+324 718 692 03</text>

      <rect class="icon" x="472" y="404" width="26" height="16"/>
      <path class="icon" d="M472 404 L485 414 L498 404"/>
      <text class="contact" x="520" y="417">mail@hedgerowpups.example</text>

      <circle class="icon" cx="485" cy="460" r="12"/>
      <ellipse class="icon" cx="485" cy="460" rx="5" ry="12"/>
      <line class="icon" x1="473" y1="460" x2="497" y2="460"/>
      <text class="contact" x="520" y="468">www.hedgerowpups.example</text>
    </g>
  </svg>

</main>
</body>
</html>
```